Plastic Business Card for Bookkeeper

We are looking for a simple professional business card design to use for printing on thin frosted plastic (see-through) card stock. Logo and brand guideline documents are attached as well as a photo of our old business card, and another business card example that we like.

Target Market(s)

Small Business

Industry/Entity Type

Bookkeeper

Contact Information for Business Card

Harriet Valdez CPA
Chief Executive Bookkeeper
T. 03 5926 4187
M. 0432 861 507
E. harriet@quillpathledger.com
W. www.quillpathledger.com

Font styles to use
Sans Serif

Colors
6b449b
00a990

Requirements
Must have
• Stick with logo colors. Writing should be clear and easy to read and not too cramped together.
Nice to have
• Tag line for back of the card - 'Not your ordinary Bookkeeper'

```html
<!DOCTYPE html>
<html lang="en">
<head>
<meta charset="utf-8">
<title>Quillpath Ledger – Business Card</title>
<link rel="stylesheet" href="https://fonts.googleapis.com/css2?family=Open+Sans:wght@400;600;700&display=swap">
<style>
  :root {
    --backdrop: #e4dfd7;
    --card-frost: #f3f1ed;
    --card-edge: #d9d4cc;
    --band-teal: #176d6e;
    --band-teal-deep: #0f5c5e;
    --brand-purple: #6b449b;
    --name-cream: #dccbaa;
    --detail-cream: #d6c9ae;
  }
  * { box-sizing: border-box; margin: 0; padding: 0; }
  html, body {
    width: 1200px;
    height: 1047px;
    overflow: hidden;
    background: var(--backdrop);
    font-family: "Open Sans", Arial, sans-serif;
  }
  .card {
    position: absolute;
    left: 80px;
    top: 240px;
    width: 1040px;
    height: 566px;
    border-radius: 26px;
    background: var(--card-frost);
    border: 2px solid var(--card-edge);
    overflow: hidden;
  }
  .brand-name {
    position: absolute;
    right: 26px;
    top: 66px;
    width: 460px;
    text-align: center;
    color: var(--brand-purple);
    font-weight: 600;
    font-size: 40px;
    line-height: 1.22;
    letter-spacing: 1px;
    text-transform: uppercase;
  }
  .info-band {
    position: absolute;
    left: 0;
    top: 214px;
    width: 770px;
    height: 352px;
    background: linear-gradient(90deg, var(--band-teal) 0%, var(--band-teal-deep) 100%);
    border-top-right-radius: 60px;
  }
  .brand-circle {
    position: absolute;
    left: 770px;
    top: 250px;
    width: 240px;
    height: 240px;
    border-radius: 50%;
    border: 12px solid var(--band-teal);
  }
  .holder-name {
    position: absolute;
    left: 60px;
    top: 246px;
    color: var(--name-cream);
    font-weight: 700;
    font-size: 40px;
    line-height: 1;
  }
  .holder-role {
    position: absolute;
    left: 60px;
    top: 300px;
    color: var(--detail-cream);
    font-size: 24px;
    line-height: 1;
  }
  .contact-list {
    position: absolute;
    left: 60px;
    top: 358px;
    list-style: none;
  }
  .contact-item {
    display: flex;
    align-items: center;
    height: 45px;
    color: var(--detail-cream);
    font-size: 24px;
  }
  .contact-icon {
    width: 22px;
    height: 22px;
    margin-right: 14px;
    fill: var(--detail-cream);
    flex: none;
  }
</style>
</head>
<body>
  <div class="card">
    <div class="brand-name">Quillpath<br>Ledger</div>

    <div class="info-band"></div>
    <div class="brand-circle"></div>

    <div class="holder-name">Valdez CPA</div>
    <div class="holder-role">Chief Executive Bookkeeper</div>

    <ul class="contact-list">
      <li class="contact-item">
        <svg class="contact-icon" viewBox="0 0 24 24"><path d="M6.6 10.8c1.4 2.8 3.8 5.1 6.6 6.6l2.2-2.2c.3-.3.7-.4 1-.2 1.1.4 2.3.6 3.6.6.6 0 1 .4 1 1V20c0 .6-.4 1-1 1C10.6 21 3 13.4 3 4c0-.6.4-1 1-1h3.5c.6 0 1 .4 1 1 0 1.3.2 2.5.6 3.6.1.3 0 .7-.2 1z"/></svg>
        03 5926 4187
      </li>
      <li class="contact-item">
        <svg class="contact-icon" viewBox="0 0 24 24"><path d="M7 1h10c1.1 0 2 .9 2 2v18c0 1.1-.9 2-2 2H7c-1.1 0-2-.9-2-2V3c0-1.1.9-2 2-2zm0 3v14h10V4zm5 15.5a1.2 1.2 0 1 0 0 2.4 1.2 1.2 0 0 0 0-2.4z"/></svg>
        0432 861 507
      </li>
      <li class="contact-item">
        <svg class="contact-icon" viewBox="0 0 24 24"><path d="M3 5h18c.6 0 1 .4 1 1v12c0 .6-.4 1-1 1H3c-.6 0-1-.4-1-1V6c0-.6.4-1 1-1zm1 3v9h16V8l-8 5z"/></svg>
        harriet@quillpathledger.com
      </li>
      <li class="contact-item">
        <svg class="contact-icon" viewBox="0 0 24 24"><path d="M12 2a10 10 0 1 0 0 20 10 10 0 0 0 0-20zm-1 17.9A8 8 0 0 1 4.1 11H7l2 2v2l2 2zm6.9-2.9c-.3-.8-1-1.5-1.9-1.5h-1v-3c0-.6-.4-1-1-1H8v-2h2c.6 0 1-.4 1-1V6h2c1.1 0 2-.9 2-2v-.4A8 8 0 0 1 17.9 17z"/></svg>
        www.quillpathledger.com
      </li>
    </ul>
  </div>
</body>
</html>
```